Young Adult novel ebook design

The book is called Label Whore: Inspired By A True StoryIt's about a wealthy male teenager who is too much into appearances, but is later humbled by a seriea of events. I need a trendy cover that resembles other top Young Adult covers, such as the examples attached. But something unique that stands out.
Target Market(s)
Teens, young adult, middle schoolers, high schoolers
Industry/Entity Type
Writer
Colors
Designer to choose colors to be used in the design.
Requirements
Must have
- Be creative and eye catching for a teenager. Leave space for the author's name. Will reveal the name to the winner.
Nice to have
- Get inspired by some of the example covers I attached.
Should not have
- No images that clearly shows a person's race. The main character image should be up for interpretation.

```html
<!DOCTYPE html>
<html lang="en">
<head>
<meta charset="utf-8">
<title>Velvet Mirror – Book Cover</title>
<link rel="stylesheet" href="https://fonts.googleapis.com/css2?family=Oswald:wght@300;400&family=Yanone+Kaffeesatz:wght@400&display=swap">
<style>
  :root {
    --backdrop-core: #0b1230;
    --backdrop-edge: #02040f;
    --paper: #f8f8f6;
    --paper-shade: #e8e8e5;
    --rule-blue: #b9c8da;
    --margin-red: #c98a8a;
    --denim-light: #c6c9ce;
    --denim-mid: #8c9097;
    --denim-dark: #3f4247;
    --label-suede: #5d5c58;
    --label-dark: #3e3d3a;
    --label-stitch: #8a8882;
    --ink: #121212;
  }
  * { margin: 0; padding: 0; box-sizing: border-box; }
  html, body { width: 1200px; height: 1000px; overflow: hidden; }
  body {
    background: radial-gradient(ellipse at 50% 50%, var(--backdrop-core) 0%, var(--backdrop-edge) 75%);
    position: relative;
  }
  .cover {
    position: absolute;
    left: 331px; top: 33px;
    width: 584px; height: 936px;
    overflow: hidden;
    background: var(--paper);
  }
  .denim-photo {
    position: absolute;
    left: 0; top: 80px;
    width: 584px; height: 470px;
    background:
      radial-gradient(ellipse 40% 30% at 15% 30%, rgba(60,63,68,0.55) 0%, transparent 100%),
      radial-gradient(ellipse 35% 25% at 85% 12%, rgba(70,72,78,0.5) 0%, transparent 100%),
      radial-gradient(ellipse 45% 30% at 75% 75%, rgba(210,212,216,0.6) 0%, transparent 100%),
      radial-gradient(ellipse 40% 30% at 20% 80%, rgba(95,98,104,0.55) 0%, transparent 100%),
      linear-gradient(160deg, var(--denim-light) 0%, var(--denim-mid) 50%, var(--denim-dark) 100%);
  }
  .label-patch {
    position: absolute;
    left: 301px; top: 307px;
    width: 410px; height: 168px;
    transform: translate(-50%, -50%) rotate(-21.5deg);
    background: radial-gradient(ellipse at 50% 50%, var(--label-suede) 0%, var(--label-dark) 100%);
    border-radius: 4px;
    box-shadow: 0 6px 14px rgba(0,0,0,0.35);
  }
  .label-patch::after {
    content: "";
    position: absolute;
    inset: 8px;
    border: 1.5px dashed var(--label-stitch);
    border-radius: 3px;
  }
  .lined-paper {
    position: absolute;
    left: 0; width: 584px;
    background:
      linear-gradient(90deg, transparent 42px, var(--margin-red) 42px, var(--margin-red) 44px, transparent 44px),
      repeating-linear-gradient(180deg, transparent 0 20px, var(--rule-blue) 20px 21.5px),
      linear-gradient(170deg, var(--paper) 0%, var(--paper-shade) 55%, var(--paper) 100%);
  }
  .paper-top {
    top: 0; height: 108px;
    clip-path: polygon(0 0, 584px 0, 584px 104px, 570px 101px, 556px 105px, 540px 100px, 524px 103px, 508px 98px, 492px 102px, 476px 97px, 460px 100px, 444px 95px, 428px 99px, 412px 94px, 396px 97px, 380px 93px, 364px 96px, 348px 92px, 332px 95px, 316px 91px, 300px 94px, 284px 90px, 268px 93px, 252px 89px, 236px 92px, 220px 88px, 204px 91px, 188px 87px, 172px 90px, 156px 86px, 140px 89px, 124px 85px, 108px 88px, 92px 84px, 76px 87px, 60px 83px, 44px 86px, 28px 82px, 14px 85px, 0 83px);
  }
  .paper-bottom {
    top: 495px; height: 441px;
    background-position: 0 0, 0 14px, 0 0;
    clip-path: polygon(0 10px, 10px 6px, 20px 9px, 32px 5px, 44px 8px, 56px 13px, 68px 11px, 80px 15px, 94px 13px, 108px 17px, 122px 15px, 136px 19px, 150px 17px, 164px 21px, 178px 19px, 192px 23px, 206px 21px, 220px 25px, 234px 23px, 248px 27px, 262px 25px, 276px 28px, 290px 26px, 304px 29px, 318px 27px, 332px 31px, 346px 29px, 360px 32px, 374px 30px, 388px 34px, 402px 32px, 416px 35px, 430px 33px, 444px 36px, 458px 34px, 472px 37px, 486px 35px, 500px 38px, 514px 36px, 528px 39px, 542px 37px, 556px 40px, 570px 38px, 584px 41px, 584px 441px, 0 441px);
  }
  .title-label {
    position: absolute;
    left: 301px; top: 300px;
    transform: translate(-50%, -50%) rotate(-21deg);
    text-align: center;
    color: var(--ink);
    white-space: nowrap;
  }
  .title-label .book-title {
    display: block;
    font-family: "Oswald", sans-serif;
    font-weight: 300;
    font-size: 54px;
    line-height: 1;
    letter-spacing: 1px;
  }
  .title-label .book-subtitle {
    display: block;
    font-family: "Oswald", sans-serif;
    font-weight: 300;
    font-size: 12px;
    letter-spacing: 5px;
    margin-top: 6px;
  }
  .author-line {
    position: absolute;
    left: 0; width: 584px; top: 828px;
    text-align: center;
    padding-left: 50px;
    font-family: "Yanone Kaffeesatz", sans-serif;
    font-variant: small-caps;
    font-size: 34px;
    letter-spacing: 1.5px;
    color: var(--ink);
  }
</style>
</head>
<body>
  <main class="cover">
    <div class="denim-photo" role="img" aria-label="Close-up photograph of faded grey denim"></div>
    <div class="label-patch"></div>
    <div class="lined-paper paper-top"></div>
    <div class="lined-paper paper-bottom"></div>
    <h1 class="title-label">
      <span class="book-title">VELVET MIRROR</span>
      <span class="book-subtitle">DRAWN FROM REAL DAYS</span>
    </h1>
    <p class="author-line">by Author Name</p>
  </main>
</body>
</html>
```